Cleaning Company Banner

Looking to have a Banner made that shows our contact information and shows what we do with good imagery to catch cars driving by. Will be a 6' x 3' banner (landscape). Attached our logo and flyer that we currently hand out.

```html
<!DOCTYPE html>
<html lang="en">
<head>
<meta charset="utf-8">
<title>BrightPath Cleaning Banner</title>
<link href="https://fonts.googleapis.com/css2?family=Bebas+Neue&family=Fredoka:wght@500;600&family=Arimo:wght@400&display=swap" rel="stylesheet">
<style>
  :root{
    --navy:#0f6795;
    --teal:#2fc4a0;
    --gold:#f0bd12;
    --pink:#f29db2;
    --mustard:#e6bf1f;
    --lime:#6cc71c;
    --sky:#4fb8ec;
    --white:#ffffff;
    --green:#5ebd1a;
  }
  *{margin:0;padding:0;box-sizing:border-box}
  html,body{width:1200px;height:833px;overflow:hidden;background:var(--white)}
  .canvas{position:relative;width:1200px;height:833px;background:var(--white)}
  .banner{position:absolute;left:116px;top:182px;width:936px;height:466px;overflow:hidden;background:var(--white)}
  .banner-bg{position:absolute;inset:0;width:936px;height:466px}
  .brand{position:absolute;left:8px;top:66px;width:204px;text-align:center;font-family:'Fredoka',sans-serif}
  .brand-name{display:flex;align-items:center;justify-content:center;gap:8px;color:var(--teal);font-weight:600;font-size:27px;letter-spacing:.5px;line-height:30px}
  .brand-mark{width:16px;height:16px;background:var(--teal)}
  .brand-sub{color:var(--teal);font-weight:600;font-size:15px;letter-spacing:2px;line-height:18px;margin-top:2px}
  .owner{position:absolute;left:0;top:136px;width:216px;text-align:center;color:var(--white);font-family:'Fredoka',sans-serif;font-weight:500;font-size:21px;line-height:26px}
  .services-title{position:absolute;left:220px;top:18px;font-family:'Bebas Neue',sans-serif;font-weight:400;font-size:54px;letter-spacing:3px;color:var(--white);line-height:1}
  .service-list{position:absolute;left:221px;top:78px;list-style:none}
  .service{display:flex;align-items:center;width:202px;height:51px;border-radius:9px;margin-bottom:11px;padding-left:12px;color:var(--white);font-family:'Fredoka',sans-serif;font-weight:500;font-size:16px;line-height:16px}
  .service svg{width:26px;height:26px;margin-right:12px;flex:none}
  .service--residential{background:var(--pink)}
  .service--commercial{background:var(--mustard)}
  .service--antiviral{background:var(--lime)}
  .service--construction{background:var(--sky)}
  .tagline{position:absolute;left:0;width:936px;top:381px;text-align:center;font-family:'Fredoka',sans-serif;font-weight:600;font-size:27.5px;color:var(--navy)}
  .tagline .gold{color:var(--gold)}
  .tagline .green{color:var(--green)}
  .contact-bar{position:absolute;left:0;bottom:0;width:936px;height:38px;background:var(--navy);display:flex;align-items:center;justify-content:center;gap:38px;color:var(--white);font-family:'Arimo',sans-serif;font-size:18px;letter-spacing:.6px}
  .contact-item{display:flex;align-items:center;gap:10px}
  .contact-item svg{width:20px;height:20px}
</style>
</head>
<body>
<div class="canvas">
  <div class="banner">
    <svg class="banner-bg" viewBox="0 0 936 466" xmlns="http://www.w3.org/2000/svg">
      <defs>
        <linearGradient id="photoTones" x1="0" y1="0" x2="1" y2="1">
          <stop offset="0" stop-color="#e9e1dc"/>
          <stop offset=".45" stop-color="#d8a6b4"/>
          <stop offset=".75" stop-color="#9fc7d6"/>
          <stop offset="1" stop-color="#6b4630"/>
        </linearGradient>
      </defs>
      <rect x="0" y="0" width="454" height="466" fill="#0f6795"/>
      <rect x="454" y="0" width="482" height="380" fill="url(#photoTones)" role="img" aria-label="Photo of cleaning supplies: spray bottles, detergent jugs, rubber gloves and sponges in a basket"/>
      <path d="M0 236 Q 470 452 936 256 L936 466 L0 466 Z" fill="#0f6795"/>
      <path d="M0 250 Q 470 476 936 270 L936 466 L0 466 Z" fill="#ffffff"/>
      <path d="M0 243 Q 235 351 469 355" fill="none" stroke="#f0bd12" stroke-width="6"/>
    </svg>

    <div class="brand">
      <div class="brand-name"><span class="brand-mark"></span>BRIGHTPATH</div>
      <div class="brand-sub">CLEANING</div>
    </div>
    <div class="owner">Dana Whitfield<br>Owner/Operator</div>

    <h2 class="services-title">Services</h2>
    <ul class="service-list">
      <li class="service service--residential">
        <svg viewBox="0 0 26 26" fill="none" stroke="#fff" stroke-width="2"><rect x="4" y="10" width="9" height="13" rx="2"/><path d="M6 10V6h5l3 2"/><rect x="16" y="14" width="7" height="9" rx="1"/></svg>
        <span>Residential<br>Cleaning</span>
      </li>
      <li class="service service--commercial">
        <svg viewBox="0 0 26 26" fill="none" stroke="#fff" stroke-width="2"><rect x="3" y="6" width="11" height="17"/><path d="M6 10h5M6 14h5M6 18h5"/><rect x="16" y="12" width="7" height="11"/></svg>
        <span>Commercial<br>Cleaning</span>
      </li>
      <li class="service service--antiviral">
        <svg viewBox="0 0 26 26" fill="none" stroke="#fff" stroke-width="2"><circle cx="8" cy="8" r="4"/><path d="M8 2v2M8 12v2M2 8h2M12 8h2"/><rect x="14" y="12" width="8" height="11" rx="2"/><path d="M16 12V9h4"/></svg>
        <span>Antiviral<br>Disinfection</span>
      </li>
      <li class="service service--construction">
        <svg viewBox="0 0 26 26" fill="none" stroke="#fff" stroke-width="2"><rect x="4" y="9" width="8" height="14" rx="2"/><path d="M6 9V5h5"/><path d="M15 23l3-10 4 1-3 9z"/></svg>
        <span>Construction<br>Cleaning</span>
      </li>
    </ul>

    <p class="tagline">Quality driven <span class="gold">and reliable</span> <span class="green">to take care of all</span> your cleaning needs!!!</p>

    <div class="contact-bar">
      <span class="contact-item">
        <svg viewBox="0 0 24 24" fill="none" stroke="#fff" stroke-width="2"><path d="M5 3h4l2 5-3 2a12 12 0 0 0 6 6l2-3 5 2v4a2 2 0 0 1-2 2A17 17 0 0 1 3 5a2 2 0 0 1 2-2z"/></svg>
        Call or Text: (555) 014-2270
      </span>
      <span class="contact-item">
        <svg viewBox="0 0 24 24" fill="none" stroke="#fff" stroke-width="1.8"><rect x="2" y="5" width="20" height="14"/><path d="M2 5l10 8 10-8"/></svg>
        hello@brightpathclean.com
      </span>
    </div>
  </div>
</div>
</body>
</html>
```